Payroll Brochure

Create a brochure with the copy i have provided . A simple easy tp read brochure that shows wat we do we handle payroll taxes insurance 401k etc

```html
<!DOCTYPE html>
<html lang="en">
<head>
<meta charset="utf-8">
<title>Brackenfold Payroll – Services Brochure</title>
<link href="https://fonts.googleapis.com/css2?family=Montserrat:wght@500;600&family=Poppins:wght@400;600&display=swap" rel="stylesheet">
<style>
  :root {
    --backdrop: #d9d8dc;
    --paper: #f5f4f2;
    --gold: #c9a033;
    --gold-light: #ecd27a;
    --accent: #8e1c1f;
    --body-text: #5a5658;
    --footer-text: #9a9698;
  }
  * { box-sizing: border-box; margin: 0; padding: 0; }
  html, body {
    width: 1200px; height: 840px; overflow: hidden;
    background: var(--backdrop);
  }
  .spread {
    position: absolute; left: 70px; top: 38px;
    width: 1060px; height: 764px;
    display: flex;
  }
  .page {
    position: relative;
    width: 530px; height: 764px;
    background: var(--paper);
    padding: 30px 34px 48px;
    font-family: "Poppins", sans-serif;
    font-size: 9.6px; line-height: 1.42;
    color: var(--body-text);
    letter-spacing: 0.02em;
  }
  .page--left { border-left: 3px solid var(--gold); border-top: 3px solid var(--gold-light); border-bottom: 3px solid var(--gold); }
  .page--right { border-right: 3px solid var(--gold); border-top: 3px solid var(--gold-light); border-bottom: 3px solid var(--gold); border-left: 1px solid #e3e1de; }
  .section-title {
    font-family: "Montserrat", sans-serif;
    font-weight: 500; font-size: 13.5px;
    letter-spacing: 0.28em; text-transform: uppercase;
    color: var(--accent); text-align: center;
    margin: 14px 0 7px;
  }
  .section-title:first-child { margin-top: 0; }
  .item { margin-bottom: 4px; }
  .item strong { color: var(--accent); font-weight: 600; }
  .site-address {
    position: absolute; left: 0; right: 0; bottom: 18px;
    text-align: center;
    font-family: "Montserrat", sans-serif; font-size: 9px;
    letter-spacing: 0.6em; text-transform: uppercase;
    color: var(--footer-text);
  }
  .offer-box {
    margin-top: 8px;
    border: 1.5px solid var(--accent); border-radius: 12px;
    padding: 8px 6px;
    text-align: center;
    font-family: "Montserrat", sans-serif; font-size: 8px;
    letter-spacing: 0.08em; text-transform: uppercase;
    color: var(--accent); line-height: 1.7;
    white-space: nowrap;
  }
</style>
</head>
<body>
<main class="spread">
  <section class="page page--left">
    <h2 class="section-title">Tax Reporting &amp; Payments</h2>
    <p class="item"><strong>Accurate</strong> – all payroll taxes (federal, state, local) are calculated accurately. Additionally, we determine proper local tax jurisdictions based on the employee home and work addresses.</p>
    <p class="item"><strong>Complete</strong> – Federal, State, and Local withholding taxes as well as State and Federal Unemployment taxes are provided. Tax payments are integrated into the Accounts Payable and General Ledger modules.</p>

    <h2 class="section-title">Human Resources</h2>
    <p class="item"><strong>With</strong> our online HR tools, you can empower yourself to take control of your human resource needs or let us do it.</p>
    <p class="item"><strong>Get Big Company Services</strong> – by using our online tools in conjunction with your service team, you will have access to HR services only afforded by some of the largest companies.</p>
    <p class="item"><strong>Library</strong> – our online document library lets you and employees create your own library of information accessible at any time. Employees can upload documents and forms that can be kept in history as long as needed.</p>

    <h2 class="section-title">Benefit Enrollment</h2>
    <p class="item"><strong>Easy and Quick Enrollment</strong> – our intuitive user experience quickly walks employees through their benefit enrollment process and allows them to compare different plans and select those that best meet their life needs.</p>
    <p class="item"><strong>Flexible Benefit Plans and Easy Setup Options</strong> – offer your clients Fortune 500 benefit plans or administer their plans in an easy to use, yet flexible benefit administration module.</p>
    <p class="item"><strong>You Pick</strong> – with our flexible contribution setup features, you can contribute in any manner to your employees' benefits while the system automatically processes them through payroll.</p>

    <h2 class="section-title">On Boarding</h2>
    <p class="item"><strong>Customize your On Boarding</strong> – you can customize your on boarding experience to your hiring needs as well as provide multiple workflows for different employee types. The on boarding experience can be branded for you providing a personalized experience for the employees.</p>
    <p class="item"><strong>Custom Document Management</strong> – our custom document mapping feature lets you use your own forms and documents as part of the on boarding and hiring process. When these forms are completed – and electronically signed – they stay in history as long as needed.</p>
    <p class="item"><strong>Intuitive</strong> – with a focus on the user experience, your employees will find it easy and quick to get on boarded with you.</p>

    <h2 class="section-title">Applicant Tracking</h2>
    <p class="item"><strong>Create and Post Jobs</strong> – you can create jobs with just a few clicks and post them on all the popular job sites.</p>
    <p class="item"><strong>Hire the Right People</strong> – by posting on popular job boards, as well as a proprietary database of job seekers, you will reach more candidates. You can choose to receive profiles of candidates that only match your background and specifications.</p>

    <p class="site-address">www.brackenfoldpayroll.com</p>
  </section>

  <section class="page page--right">
    <p class="item"><strong>Manage the Hiring Process</strong> – review candidates via video or online conferencing, review voice interviews, schedule in person interviews, have candidates answer certain online questions, and manage this entire process to find the right people. Once hired, they can be on boarded automatically.</p>

    <h2 class="section-title">Time and Attendance</h2>
    <p class="item"><strong>Make Time Entry Easy</strong> – Simplify time tracking so you can spend less time on payroll tasks.</p>
    <p class="item"><strong>Everywhere Access</strong> – Web interface, mobile apps, and on-premise time clocks allow employees to log their time wherever they are.</p>
    <p class="item"><strong>Plug and Play Time Clocks</strong> – Time clocks are delivered ready-to-use with little or no setup required.</p>

    <h2 class="section-title">ACA Compliance</h2>
    <p class="item"><strong>Client Tools</strong> – provide you with reporting and analysis tools online so you can monitor ACA information and be proactive in managing your needs.</p>
    <p class="item"><strong>Affordability Test</strong> – provide your with information about plan affordability with their employees so they can stay in compliance.</p>
    <p class="item"><strong>Large Employer Analysis</strong> – analyze your control groups to determine if you will fall under the rules of ACA for large employer groups.</p>

    <h2 class="section-title">Self Service</h2>
    <p class="item"><strong>Manager</strong> – your managers have access to their information via a highly intuitive online portal. Users can enter payroll time, create ad-hoc reports, preview and approve payroll and invoices, get invoice and check history, access employee records, communicate with employees, create, etc. Our single sign on allows managers that may have multiple business entities with Brackenfold umbrella to use one login.</p>
    <p class="item"><strong>Employee</strong> – employees can access pay information, request PTO, enroll in benefits, communicate with other employees, and access/change their personal information. They can also access corporate documents for review and upload personal documents as well.</p>

    <h2 class="section-title">WOTC</h2>
    <p class="item"><strong>Big Credits</strong> – Work Opportunity Tax Credits (WOTC) allow you to receive between $2,400 and $9,600 for hiring eligible employees.</p>
    <p class="item"><strong>Easy and Quick</strong> – Employees complete a simple questionnaire to determine eligibility for WOTC. All of the necessary filing and reporting is handled for you and your client.</p>
    <p class="item"><strong>Integrated</strong> – WOTC is integrated wherever you would enter a new employee – back office payroll, online on boarding, and applicant tracking to ensure all employees are being evaluated.</p>

    <h2 class="section-title">Workers Compensation and Benefits</h2>
    <div class="offer-box">
      <p>Pay as you go workers' compensation – multiple carriers available</p>
      <p>Access to a multiple employer 401k</p>
      <p>Access to various voluntary benefits</p>
    </div>

    <p class="site-address">www.brackenfoldpayroll.com</p>
  </section>
</main>
</body>
</html>
```